Lunaryth needs a elegant mystical business card design

The theme of Lunaryth is centered on Kemetic/Ancient Egyptian Spirituality. My business sells handmade scented candles, mystic oils, body sprays, tarot readings and more. I would like my business card to reflect an elegant and mystical look. Hieroglyphs around the borders would be a cool idea. Also, the main colors I am working with is Black and Gold= colors of royalty. Black background. The business card will be double sided. The back will have the logo, and the front will have the basic information (ie name, title, business, phone, email, website, etc..)

Target Market(s)

The target market are people into metaphysics, holistic healing, ancient Egyptian culture, aromatherapy, occult science, and the esoteric.

Industry/Entity Type

Business

Contact Information for Business Card

Name: Marisol T. Pike
Title: Owner
Business: LUNARYTH
Phone: 555.210.4473
Website: www.Lunaryth.example
Facebook, Instagram, and twitter icons

Font styles to use
Serif
Decorative

Requirements
Must have
• My logo, and website.
Nice to have
• Ancient Egyptian hieroglyphs, Elegant designs around the border, or encircling the logo.

```html
<!DOCTYPE html>
<html lang="en">
<head>
<meta charset="utf-8">
<title>Lunaryth Business Card</title>
<link href="https://fonts.googleapis.com/css2?family=Open+Sans:wght@400;600&display=swap" rel="stylesheet">
<style>
  :root {
    --backdrop: #2b2624;
    --card-black: #1c1c1d;
    --card-black-edge: #262627;
    --gold: #c9a064;
    --gold-light: #c6a571;
    --gold-dark: #8b6a3f;
    --white: #f4f1ec;
    --divider: #3a3a3b;
  }
  html, body {
    margin: 0;
    padding: 0;
    width: 1200px;
    height: 844px;
    overflow: hidden;
    background: var(--backdrop);
    font-family: "Open Sans", Arial, sans-serif;
  }
  .canvas {
    position: relative;
    width: 1200px;
    height: 844px;
  }
  .card {
    position: absolute;
    top: 274px;
    width: 520px;
    height: 297px;
    border-radius: 4px;
    overflow: hidden;
    box-shadow: 0 10px 28px rgba(0,0,0,0.45);
  }
  /* Information side */
  .card-info {
    left: 50px;
    background: linear-gradient(160deg, var(--card-black-edge), var(--card-black));
  }
  .info-brand {
    position: absolute;
    left: 30px;
    top: 128px;
    width: 200px;
    text-align: center;
    color: var(--gold);
    font-weight: 600;
    font-size: 24px;
    letter-spacing: 3px;
  }
  .info-divider {
    position: absolute;
    left: 258px;
    top: 70px;
    width: 1px;
    height: 130px;
    background: var(--divider);
  }
  .contact-block {
    position: absolute;
    left: 280px;
    top: 80px;
  }
  .person-name {
    margin: 0;
    color: var(--gold);
    font-weight: 600;
    font-size: 17px;
    line-height: 1.2;
  }
  .person-title {
    margin: 2px 0 0;
    color: var(--white);
    font-size: 11px;
  }
  .contact-list {
    list-style: none;
    margin: 24px 0 0;
    padding: 0;
  }
  .contact-list li {
    display: flex;
    align-items: center;
    gap: 9px;
    color: var(--white);
    font-size: 12px;
    line-height: 20px;
  }
  .contact-icon {
    width: 10px;
    height: 10px;
    flex: none;
  }
  .social-row {
    position: absolute;
    left: 280px;
    top: 232px;
    display: flex;
    gap: 8px;
  }
  .social-square {
    width: 22px;
    height: 22px;
    border-radius: 3px;
    background: var(--gold);
  }
  /* Brand side */
  .card-brand {
    left: 630px;
    background: linear-gradient(165deg, var(--gold-light) 0%, #ac8853 55%, var(--gold-dark) 100%);
  }
  .brand-flourish {
    position: absolute;
    left: 40px;
    top: 60px;
    width: 180px;
    height: 200px;
    border-radius: 50%;
    background: radial-gradient(ellipse at center, rgba(140,105,60,0.35), rgba(140,105,60,0) 70%);
  }
  .brand-name {
    position: absolute;
    left: 0;
    right: 0;
    top: 128px;
    text-align: center;
    color: var(--white);
    font-weight: 600;
    font-size: 34px;
    letter-spacing: 5px;
  }
</style>
</head>
<body>
<main class="canvas">
  <section class="card card-info" aria-label="Card information side">
    <div class="info-brand">LUNARYTH</div>
    <div class="info-divider"></div>
    <div class="contact-block">
      <h1 class="person-name">Marisol T. Pike</h1>
      <p class="person-title">Owner</p>
      <ul class="contact-list">
        <li>
          <svg class="contact-icon" viewBox="0 0 10 10" aria-hidden="true">
            <path d="M2 0.8 L3.6 2.8 L2.8 3.8 Q4 6 6.2 7.2 L7.2 6.4 L9.2 8 L8 9.4 Q3.5 9 0.6 2 Z" fill="var(--gold)"/>
          </svg>
          555.210.4473
        </li>
        <li>
          <svg class="contact-icon" viewBox="0 0 10 10" aria-hidden="true">
            <circle cx="5" cy="5" r="4.5" fill="var(--gold)"/>
            <path d="M0.8 5 H9.2 M5 0.6 Q2.5 5 5 9.4 M5 0.6 Q7.5 5 5 9.4" stroke="var(--card-black)" stroke-width="0.8" fill="none"/>
          </svg>
          www.Lunaryth.example
        </li>
      </ul>
    </div>
    <div class="social-row" aria-label="Social media">
      <span class="social-square"></span>
      <span class="social-square"></span>
      <span class="social-square"></span>
    </div>
  </section>

  <section class="card card-brand" aria-label="Card brand side">
    <div class="brand-flourish" role="img" aria-label="Faint tone-on-tone floral flourish"></div>
    <div class="brand-name">LUNARYTH</div>
  </section>
</main>
</body>
</html>
```